Business Card Design Project

I have just chosen a logo and would now like this designed onto a business card for my hair salon. I would like it to be classy not to busy and have a wow factor when people look at them
Has to Include on card:
Logo Design
And business details below
Kellie-ann Drummond (owner)
0482 736 219
Rdw@vomblet.com.au
71 Willowmere Rise Corvin Cove
Logo is now attached please provide designs
Hair

```html
<!DOCTYPE html>
<html lang="en">
<head>
<meta charset="utf-8">
<title>Maribel Hair Studio – Business Cards</title>
<link rel="stylesheet" href="https://fonts.googleapis.com/css2?family=Jost:wght@400;500&display=swap">
<style>
  :root {
    --backdrop: #e4e0dc;
    --card-paper: #eeeeee;
    --brand-ink: #c8166f;
    --contact-ink: #ffffff;
    --pink: #e8388f;
    --blue: #3550a3;
    --red: #e3312d;
  }
  html, body {
    margin: 0;
    padding: 0;
    width: 1200px;
    height: 946px;
    overflow: hidden;
    background: var(--backdrop);
    font-family: "Jost", sans-serif;
  }
  .card-sheet {
    position: relative;
    width: 1200px;
    height: 946px;
  }
  .business-card {
    position: absolute;
    width: 520px;
    height: 300px;
    background: var(--card-paper);
    box-shadow: 0 6px 18px rgba(0,0,0,0.18);
    overflow: hidden;
  }
  .business-card--pink { --accent: var(--pink); left: 50px;  top: 70px; }
  .business-card--blue { --accent: var(--blue); left: 630px; top: 70px; }
  .business-card--red  { --accent: var(--red);  left: 340px; top: 560px; }

  .colour-sweep {
    position: absolute;
    inset: 0;
    width: 100%;
    height: 100%;
  }
  .colour-sweep path { fill: var(--accent); }

  .brand-name {
    position: absolute;
    top: 34px;
    right: 62px;
    display: flex;
    align-items: center;
    gap: 10px;
    color: var(--brand-ink);
    font-weight: 500;
    font-size: 28px;
    letter-spacing: 0.5px;
    line-height: 1;
  }
  .brand-dot {
    width: 12px;
    height: 12px;
    border-radius: 50%;
    background: var(--brand-ink);
  }

  .contact-details {
    position: absolute;
    right: 40px;
    top: 138px;
    margin: 0;
    padding: 0;
    list-style: none;
    text-align: right;
    color: var(--contact-ink);
    font-weight: 400;
    font-size: 17px;
    line-height: 27px;
  }
  .contact-details .phone { font-size: 20px; }
</style>
</head>
<body>
<main class="card-sheet">

  <article class="business-card business-card--pink">
    <svg class="colour-sweep" viewBox="0 0 520 300" preserveAspectRatio="none" aria-hidden="true">
      <path d="M0 112 C150 112 300 170 420 100 C465 72 500 38 520 18 L520 272 L0 272 Z"/>
    </svg>
    <div class="brand-name"><span class="brand-dot"></span>Maribel Hair Studio</div>
    <ul class="contact-details">
      <li>Kellie-ann Drummond (owner)</li>
      <li class="phone">0482 736 219</li>
      <li>Rdw@vomblet.com.au</li>
      <li>71 Willowmere Rise Corvin Cove</li>
    </ul>
  </article>

  <article class="business-card business-card--blue">
    <svg class="colour-sweep" viewBox="0 0 520 300" preserveAspectRatio="none" aria-hidden="true">
      <path d="M0 112 C150 112 300 170 420 100 C465 72 500 38 520 18 L520 272 L0 272 Z"/>
    </svg>
    <div class="brand-name"><span class="brand-dot"></span>Maribel Hair Studio</div>
    <ul class="contact-details">
      <li>Kellie-ann Drummond (owner)</li>
      <li class="phone">0482 736 219</li>
      <li>Rdw@vomblet.com.au</li>
      <li>71 Willowmere Rise Corvin Cove</li>
    </ul>
  </article>

  <article class="business-card business-card--red">
    <svg class="colour-sweep" viewBox="0 0 520 300" preserveAspectRatio="none" aria-hidden="true">
      <path d="M0 112 C150 112 300 170 420 100 C465 72 500 38 520 18 L520 272 L0 272 Z"/>
    </svg>
    <div class="brand-name"><span class="brand-dot"></span>Maribel Hair Studio</div>
    <ul class="contact-details">
      <li>Kellie-ann Drummond (owner)</li>
      <li class="phone">0482 736 219</li>
      <li>Rdw@vomblet.com.au</li>
      <li>71 Willowmere Rise Corvin Cove</li>
    </ul>
  </article>

</main>
</body>
</html>
```